Bref créative
Business Cards/Letterhead for a Private Equity Real Estate Company
KTR Commercial
Simple
H. Dalton Greave
President
4780 Brambling Road
Suite 610
Atlanta, GA 30342
dalton@ktrcommercial.net
http://ktrcommercial.net/
We think we want the logo on one side and then all the written information on the other. Open to seeing different suggestions, though. Thanks for everyone who participates!

```html
<!DOCTYPE html>
<html lang="en">
<head>
<meta charset="utf-8">
<title>KTR Commercial – Business Card</title>
<link rel="stylesheet" href="https://fonts.googleapis.com/css2?family=Arimo:wght@400;700&display=swap">
<style>
  :root {
    --page-bg: #d9d9d9;
    --card-white: #ffffff;
    --card-dark-top: #5b5b5b;
    --card-dark-bottom: #232323;
    --ink: #2b2b2b;
    --ink-soft: #555555;
    --accent-red: #c8202a;
    --on-dark: #f2f2f2;
  }
  * { box-sizing: border-box; margin: 0; padding: 0; }
  html, body {
    width: 1200px; height: 901px; overflow: hidden;
    background: var(--page-bg);
    font-family: "Arimo", Arial, sans-serif;
  }
  .sheet {
    width: 1200px; height: 901px;
    display: flex; align-items: center; justify-content: center; gap: 60px;
  }
  .card {
    width: 520px; height: 297px;
    position: relative;
    box-shadow: 0 6px 18px rgba(0,0,0,0.18);
  }
  .card--back {
    background: linear-gradient(160deg, var(--card-dark-top), var(--card-dark-bottom));
    display: flex; align-items: center; justify-content: center;
  }
  .card--front { background: var(--card-white); }

  .brand {
    display: flex; align-items: center; justify-content: center; gap: 12px;
  }
  .brand__square {
    width: 16px; height: 16px; background: var(--accent-red); flex: none;
  }
  .brand__name {
    font-weight: 700; font-size: 34px; letter-spacing: 1px;
    color: var(--ink); white-space: nowrap;
  }
  .card--back .brand__name { color: var(--on-dark); }

  .card--front .brand { position: absolute; top: 56px; left: 0; right: 0; }

  .details {
    position: absolute; left: 30px; right: 30px; bottom: 44px;
    display: flex; justify-content: center; gap: 22px;
  }
  .person { text-align: right; color: var(--ink); font-size: 11px; line-height: 1.45; }
  .person__name { font-weight: 700; font-size: 15px; line-height: 1.2; }
  .person__title { font-size: 10px; color: var(--ink-soft); margin-bottom: 6px; }

  .contact { list-style: none; font-size: 11px; line-height: 1.45; color: var(--ink); padding-top: 2px; }
  .contact li { display: flex; align-items: center; gap: 7px; white-space: nowrap; }
  .contact svg { width: 10px; height: 10px; fill: var(--accent-red); flex: none; }
</style>
</head>
<body>
  <main class="sheet">
    <section class="card card--back" aria-label="Card back">
      <div class="brand">
        <span class="brand__square"></span>
        <span class="brand__name">KTR Commercial</span>
      </div>
    </section>

    <section class="card card--front" aria-label="Card front">
      <div class="brand">
        <span class="brand__square"></span>
        <span class="brand__name">KTR Commercial</span>
      </div>

      <div class="details">
        <div class="person">
          <div class="person__name">H. Dalton Greave</div>
          <div class="person__title">President</div>
          <div>4780 Brambling Road, Suite 610</div>
          <div>Atlanta, GA 30342</div>
        </div>
        <ul class="contact">
          <li>
            <svg viewBox="0 0 10 10"><path d="M1 2.5C1 1.7 1.7 1 2.5 1h5C8.3 1 9 1.7 9 2.5V4H7V3H3v1H1z"/><rect x="2" y="5" width="6" height="4" rx="0.6"/></svg>
            (404) 555-0142
          </li>
          <li>
            <svg viewBox="0 0 10 10"><path d="M3 0.5h4a1 1 0 0 1 1 1v7a1 1 0 0 1-1 1H3a1 1 0 0 1-1-1v-7a1 1 0 0 1 1-1zM3 2v5.5h4V2z"/></svg>
            (404) 555-0187
          </li>
          <li>
            <svg viewBox="0 0 10 10"><path d="M0.5 2h9v6h-9zM1.5 3v0.4L5 5.8l3.5-2.4V3L5 5.2z"/></svg>
            dalton@ktrcommercial.net
          </li>
          <li>
            <svg viewBox="0 0 10 10"><path d="M5 0.5a4.5 4.5 0 1 0 0 9a4.5 4.5 0 0 0 0-9zM5 1.6c.6.7 1 1.7 1.1 2.9H3.9C4 3.3 4.4 2.3 5 1.6zM3.9 5.5h2.2C6 6.7 5.6 7.7 5 8.4 4.4 7.7 4 6.7 3.9 5.5zM1.6 4.5a3.4 3.4 0 0 1 1.8-2.6c-.3.7-.5 1.6-.6 2.6zm0 1h1.2c.1 1 .3 1.9.6 2.6A3.4 3.4 0 0 1 1.6 5.5zm5.6 0h1.2a3.4 3.4 0 0 1-1.8 2.6c.3-.7.5-1.6.6-2.6zm0-1c-.1-1-.3-1.9-.6-2.6a3.4 3.4 0 0 1 1.8 2.6z"/></svg>
            www.ktrcommercial.net
          </li>
        </ul>
      </div>
    </section>
  </main>
</body>
</html>
```